Pivora has a great new logo - now we need a website!!

Pivora has been in business for a long time and needs to start a new era. Additional to other changes being made in the business itself, Pivora needs an overhaul of its entire branding. PART 1 is COMPLETE - we have our new logo!

Next step... new website! That's where you come in.

Pivora provides a range of computer related services including computer maintenance, networking, sales & cloud services. We provide onsite (field) and remote support. Our customers range from homes to companies with 100+ computers. We pride ourselves on clear and honest communication.

We are a small business but want a professional yet easy-going look that shows the 'cool' side of having your computer system cared for. The website should exude trustworthiness and professionalism but still get comments like 'modern' and 'smart design'. We want our customers to feel that choosing any other company to maintain their system would be a 'geeky' choice.

We like clear thinking so an uncluttered, well organised structure is appreciated. Obvious references to calling or emailing us would be good so people dont need to search around for our contact details.

We look after both Quince & Veltharon operating systems so there needs to be universal appeal rather than a look associated with only one of these two brands.

We want to wow our current clients but also attract new ones so a focus on SEO is a must. And a focus on social media too with links/feeds to Chatterly, chirpex and WorkLoop!

Have a look at www.pivora.com.au so you can see for yourself how much you can help us!

**Breathe new life into Pivora's online presence!**

(We do have a separate website www.kelbrohome.com.au that we set as the homepage for our clients - we like how it is but it might need freshening up to match our new site. We will also want our chatterly page totally made over. You'll probably have other suggestions of things we should be doing. We want to form an ongoing relationship with the right designer!)

(Also, we are open to suggestions regarding the logo size and colour)
Updates

I dont want to cramp anyones creativity but i like this: http://www.quindlework.com/demo/themes/wordpress/2011/saffron/

I'm obivously happy to see your own ideas too!

I also like this one: http://marbleloft.net/item/dralo-responsive-wordpress-theme/7184206

Clarification: We are looking for a working, implemented website, not just design of the theme. Once the general page layout is done we can do the majority of the content input. But we do want a workable shell with images.

We are open to buying existing themes if that helps. Thanks!

Site also needs email contact form, testimonial submission page, blog (feed to home page), chatterly like button

Reason: I haven't found the ideal one yet... We want some other designers to send their ideas.

Reason: We need a little more time to make our decision.

Target Market(s)

Mainly small to medium businesses but also homes

Industry/Entity Type

Small Business

Requirements
Must have
• SEO
Social Media
That little address bar icon
R in a circle at the bottom of the site to show we have trademarked our company name
A finished product website with content and images that we can modify ourselves over time.

```html
<!DOCTYPE html>
<html lang="en">
<head>
<meta charset="utf-8">
<title>Pivora – IT Solutions &amp; Support</title>
<link href="https://fonts.googleapis.com/css2?family=PT+Sans:wght@400;700&family=Open+Sans:wght@400;600;700&display=swap" rel="stylesheet">
<style>
:root{
  --topbar:#34305f;
  --purple-dark:#3f3285;
  --link:#4f3f9a;
  --text:#555a63;
  --muted:#8a8e96;
  --rule:#e2e3e6;
  --green:#8cc63e;
  --green-dark:#6ea52a;
  --white:#ffffff;
}
*{box-sizing:border-box;margin:0;padding:0}
html,body{width:851px;height:1200px;overflow:hidden}
body{position:relative;background:var(--white);font-family:"Open Sans",Arial,sans-serif;color:var(--text);font-size:9px;line-height:1.55}
.abs{position:absolute}
a{color:inherit;text-decoration:none}

/* top bar */
.topbar{left:0;top:0;width:851px;height:21px;background:var(--topbar);color:#d9d6ee;font-size:8px}
.topbar .links{left:91px;top:5px;display:flex}
.topbar .links span{padding:0 6px;border-left:1px solid #55508a}
.topbar .links span:first-child{padding-left:0;border:0;color:#fff}
.topbar .social{right:108px;top:5px;display:flex;gap:14px;color:#fff;font-weight:600}
.topbar .social span{display:flex;align-items:center;gap:4px}
.ico{width:9px;height:9px;display:inline-block}

/* header */
.header{left:0;top:21px;width:851px;height:75px;background:linear-gradient(#fff,#f6f6f8);border-bottom:1px solid #ddd}
.brand{left:91px;top:34px;display:flex;align-items:center;gap:8px}
.brand .mark{width:30px;height:30px;border-radius:50%;background:var(--purple-dark)}
.brand .name{font-family:"PT Sans",sans-serif;font-weight:700;font-size:24px;color:#2c2f3a;line-height:1}
.brand-tagline{left:130px;top:58px;font-size:8px;color:#7a7f88}
.nav{top:51px;left:0;font-family:"PT Sans",sans-serif;font-size:12px;color:#6c6f78}
.nav span{position:absolute;white-space:nowrap}
.nav .current{color:var(--link)}

/* hero */
.hero{left:0;top:96px;width:851px;height:228px;background:radial-gradient(ellipse at 30% 40%,#6e5cc0 0%,#5643a4 55%,#43358f 100%)}
.hero-title{left:91px;top:138px;font-family:"PT Sans",sans-serif;font-size:18px;line-height:24px;color:#fff;font-weight:400}
.hero-copy{left:91px;top:168px;width:320px;color:#ece9fb;font-size:8.5px;line-height:1.6}
.btn{display:flex;align-items:center;justify-content:center;border-radius:3px;font-size:8.5px;color:#fff;background:linear-gradient(var(--green),var(--green-dark));border:1px solid #5f9322}
.hero-btn{left:91px;top:234px;width:112px;height:19px}
.video-frame{left:424px;top:117px;width:307px;height:184px;background:#fff;padding:6px;box-shadow:0 2px 6px rgba(0,0,0,.3)}
.video-art{width:100%;height:100%;background:radial-gradient(circle at 45% 40%,#d9f07a,#a9d22e 70%);position:relative}
.video-bar{position:absolute;left:8px;right:8px;bottom:8px;height:22px;display:flex;gap:4px}
.video-bar .play{width:34px;background:rgba(20,22,28,.85);border-radius:2px;display:flex;align-items:center;justify-content:center}
.video-bar .track{flex:1;background:rgba(20,22,28,.85);border-radius:2px;position:relative}
.video-bar .track i{position:absolute;left:6px;right:60px;top:9px;height:4px;background:#555a62}
.dots{display:flex;gap:5px}
.dots b{width:6px;height:6px;border-radius:50%;background:#cfd0d4}
.dots b.on{background:#9ea0a6}
.hero-dots{left:404px;top:337px}

/* features */
.feature-img{top:371px;width:194px;height:96px;border:1px solid #e2e2e2;padding:4px;background:#fff;box-shadow:0 1px 3px rgba(0,0,0,.12)}
.feature-img div{width:100%;height:100%}
.feature-title{top:480px;font-family:"PT Sans",sans-serif;font-size:10.5px;font-weight:400;color:var(--link)}
.feature-copy{top:500px;width:196px;font-size:8.5px}
.rule{height:1px;background:var(--rule)}

/* blog + testimonial */
.label{font-size:7px;text-transform:uppercase;letter-spacing:.3px;color:#5b5f68}
.post{width:320px;padding-left:18px}
.post h4{font-family:"PT Sans",sans-serif;font-size:9px;color:var(--link);font-weight:700}
.post p{font-size:8.5px}
.bubble{position:absolute;left:0;top:2px;width:10px;height:8px}
.quote{width:280px;padding-left:18px;color:#7a7f88;font-size:8.5px}
.quote-mark{position:absolute;left:0;top:-4px;font-family:"PT Sans",sans-serif;font-size:22px;color:#cfd1d6;line-height:1}

/* callout */
.callout{left:0;top:918px;width:851px;height:85px;background:linear-gradient(#fafafa,#ececef);border-top:1px solid #e2e2e2}
.callout-title{left:135px;top:941px;font-family:"PT Sans",sans-serif;font-size:13px;font-weight:400;color:var(--link)}
.callout-copy{left:135px;top:960px;font-size:11px;color:var(--muted);font-family:"PT Sans",sans-serif}
.callout-btn{left:658px;top:948px;width:117px;height:25px;font-size:9px}

/* footer */
.footer{left:0;top:1003px;width:851px;height:197px;background:radial-gradient(ellipse at 40% 30%,#6553b7,#4a3a96 60%,#3b2f84)}
.footer-brand{left:135px;top:1036px;display:flex;align-items:center;gap:6px;font-family:"PT Sans",sans-serif;font-size:15px;color:#fff}
.footer-brand i{width:22px;height:22px;border-radius:50%;background:#d4cff0;display:block}
.footer-copy{left:135px;top:1069px;width:210px;color:#fff;font-size:8.5px}
.footer-h{font-family:"PT Sans",sans-serif;font-size:10.5px;font-weight:400;color:#fff}
.field-label{left:441px;top:1066px;color:#d8d3f5;font-size:8.5px}
.field{left:441px;top:1083px;width:122px;height:19px;background:#fff;border:1px solid #ccc}
.subscribe{left:441px;top:1117px;width:51px;height:18px;background:#f3f3f5;border-radius:3px;color:#444;font-size:8px;display:flex;align-items:center;justify-content:center}
.footer-social{left:608px;top:1063px;display:flex;gap:12px;color:#fff;font-size:8.5px}
.footer-social span{display:flex;align-items:center;gap:4px}
.footer-bottom{left:0;top:1168px;width:851px;height:32px;background:rgba(30,24,70,.35);color:#fff;font-size:7.5px}
.footer-bottom .copy{left:135px;top:11px}
.footer-bottom .menu{left:470px;top:11px;display:flex}
.footer-bottom .menu span{padding:0 6px;border-left:1px solid #7a70b8}
.footer-bottom .menu span:first-child{border:0}
.footer-bottom .top{left:719px;top:11px}
</style>
</head>
<body>

<header>
  <div class="abs topbar">
    <nav class="abs links"><span>Home</span><span>Team</span><span>Sitemap</span><span>Testimonials</span><span>Contact</span></nav>
    <div class="abs social">
      <span>☎ 1300 555 274</span>
      <span><svg class="ico" viewBox="0 0 10 10"><circle cx="5" cy="5" r="4" fill="#7fc6ea"/></svg>chirpex</span>
      <span><svg class="ico" viewBox="0 0 10 10"><rect width="10" height="10" rx="1" fill="#dfe3f3"/></svg>Chatterly</span>
      <span><svg class="ico" viewBox="0 0 10 10"><path d="M1 2h8v5H4l-2 2V7H1z" fill="#fff"/></svg>Email</span>
    </div>
  </div>

  <div class="abs header"></div>
  <div class="abs brand"><span class="mark"></span><span class="name">Pivora</span></div>
  <div class="abs brand-tagline">IT Solutions &amp; Support</div>
  <nav class="abs nav">
    <span class="current" style="left:322px">Home</span>
    <span style="left:372px">Services</span>
    <span style="left:436px">Support</span>
    <span style="left:500px">Gallery</span>
    <span style="left:560px">Testimonials</span>
    <span style="left:652px">Blog</span>
    <span style="left:696px">Contact</span>
  </nav>
</header>

<section class="hero-block">
  <div class="abs hero"></div>
  <h1 class="abs hero-title">Computer Care, Made Easy!</h1>
  <p class="abs hero-copy">Pivora looks after your computers so you don't have to. From maintenance and networking to sales and cloud services, we support homes and businesses with 100+ computers, onsite or remotely, with clear and honest communication every step of the way.</p>
  <a class="abs btn hero-btn">Book a Service Call →</a>
  <div class="abs video-frame">
    <div class="video-art" role="img" aria-label="Introductory video still about Pivora computer support">
      <div class="video-bar">
        <div class="play"><svg width="10" height="10" viewBox="0 0 10 10"><path d="M2 1l7 4-7 4z" fill="#fff"/></svg></div>
        <div class="track"><i></i></div>
      </div>
    </div>
  </div>
  <div class="abs dots hero-dots"><b class="on"></b><b></b><b></b></div>
</section>

<section class="features">
  <div class="abs feature-img" style="left:91px"><div role="img" aria-label="Photo of balanced stones with a green leaf" style="background:linear-gradient(135deg,#e6f3c9,#9ccb3e 60%,#8a5a3a)"></div></div>
  <div class="abs feature-img" style="left:313px"><div role="img" aria-label="Photo of a person working on a laptop" style="background:linear-gradient(135deg,#5f84b8,#c9dcef 55%,#e9d7c4)"></div></div>
  <div class="abs feature-img" style="left:535px"><div role="img" aria-label="Photo of a computer mouse on a desk" style="background:linear-gradient(135deg,#f2f2f2,#bfc4c9 55%,#6c7178)"></div></div>

  <h3 class="abs feature-title" style="left:91px">Computer Maintenance</h3>
  <h3 class="abs feature-title" style="left:313px">Networking &amp; Cloud Services</h3>
  <h3 class="abs feature-title" style="left:534px">Onsite &amp; Remote Support</h3>

  <p class="abs feature-copy" style="left:91px">Regular health checks, updates and backups keep your machines fast and safe. We look after Quince and Veltharon systems alike.</p>
  <p class="abs feature-copy" style="left:313px">Reliable office networks, secure Wi-Fi and cloud email and storage, set up properly and explained in plain English.</p>
  <p class="abs feature-copy" style="left:534px">We come to you or fix it remotely, whichever is quickest. Call 1300 555 274 or email help@pivora.com.au for fast help.</p>

  <div class="abs rule" style="left:91px;top:582px;width:640px"></div>
</section>

<section class="news">
  <div class="abs label" style="left:91px;top:598px">Latest from the blog</div>
  <div class="abs post" style="left:91px;top:619px">
    <svg class="bubble" viewBox="0 0 10 8"><path d="M0 0h10v6H3L1 8V6H0z" fill="#c9ccd3"/></svg>
    <h4>Is Your Network Ready for the Cloud?</h4>
    <p>Moving email and files online saves time and money. Here is a simple checklist to see if your office is ready to go...</p>
  </div>
  <div class="abs post" style="left:91px;top:673px">
    <svg class="bubble" viewBox="0 0 10 8"><path d="M0 0h10v6H3L1 8V6H0z" fill="#c9ccd3"/></svg>
    <h4>Five Backup Habits Worth Keeping</h4>
    <p>Losing files is stressful and avoidable. These five easy habits keep your photos, invoices and records safe every day...</p>
  </div>
  <div class="abs label" style="left:454px;top:598px">Our clients say it best</div>
  <div class="abs quote" style="left:454px;top:618px"><span class="quote-mark">“</span>Thanks so much for fixing my issue so quickly, I would just like to say that your company has provided such amazing customer service/ support to date it has really blown me away (it is very rare in business today)</div>
  <div class="abs dots" style="left:698px;top:677px"><b></b><b></b><b class="on"></b></div>

  <div class="abs rule" style="left:135px;top:742px;width:640px"></div>

  <div class="abs label" style="left:135px;top:759px">Tips &amp; news</div>
  <div class="abs post" style="left:135px;top:780px">
    <svg class="bubble" viewBox="0 0 10 8"><path d="M0 0h10v6H3L1 8V6H0z" fill="#c9ccd3"/></svg>
    <h4>Quince or Veltharon? We Support Both</h4>
    <p>Whatever your team uses, Pivora keeps it running smoothly. Find out how we manage mixed offices without the fuss...</p>
  </div>
  <div class="abs post" style="left:135px;top:834px">
    <svg class="bubble" viewBox="0 0 10 8"><path d="M0 0h10v6H3L1 8V6H0z" fill="#c9ccd3"/></svg>
    <h4>Spotting a Slow Computer Early</h4>
    <p>Long start-up times and noisy fans are early warnings. Learn the signs and when it is time to give us a call...</p>
  </div>
  <div class="abs label" style="left:498px;top:759px">Share your experience</div>
  <div class="abs quote" style="left:498px;top:779px"><span class="quote-mark">“</span>Pivora set up our whole office network in a day and explained everything clearly. No jargon, no fuss, just great service!</div>
  <div class="abs dots" style="left:745px;top:838px"><b></b><b class="on"></b><b></b></div>
</section>

<section class="callout-block">
  <div class="abs callout"></div>
  <h2 class="abs callout-title">Need a hand with your computers?</h2>
  <p class="abs callout-copy">Call 1300 555 274 or email help@pivora.com.au and we'll get you sorted.</p>
  <a class="abs btn callout-btn">Contact Pivora →</a>
</section>

<footer>
  <div class="abs footer"></div>
  <div class="abs footer-brand"><i></i>Pivora</div>
  <p class="abs footer-copy">Pivora provides computer maintenance, networking, sales and cloud services for homes and small to medium businesses, onsite and remote.</p>

  <h4 class="abs footer-h" style="left:441px;top:1038px">Join our Mailing List</h4>
  <div class="abs field-label">Email Address</div>
  <div class="abs field"></div>
  <div class="abs subscribe">Subscribe</div>

  <h4 class="abs footer-h" style="left:608px;top:1038px">Connect with us</h4>
  <div class="abs footer-social">
    <span><svg class="ico" viewBox="0 0 10 10"><circle cx="5" cy="5" r="4" fill="#7fc6ea"/></svg>chirpex</span>
    <span><svg class="ico" viewBox="0 0 10 10"><rect width="10" height="10" rx="1" fill="#dfe3f3"/></svg>Chatterly</span>
    <span><svg class="ico" viewBox="0 0 10 10"><rect width="10" height="10" rx="1" fill="#b9c7e6"/></svg>WorkLoop</span>
  </div>

  <div class="abs footer-bottom">
    <div class="abs copy">Copyright © 2012 Pivora®. All rights reserved.</div>
    <nav class="abs menu"><span>Services</span><span>Support</span><span>Gallery</span><span>Testimonials</span><span>Blog</span><span>Contact</span></nav>
    <div class="abs top">↑ Scroll to Top</div>
  </div>
</footer>

</body>
</html>
```